I need a label design for Honey

Tropical Theme Logo designed for a Beekeeping Company.
5 Labels for Honey.
Business Cards
“Sun Orchard”

A Tropical themed logo, either palm tree or bee.

Style of text should be Brush Script italic or something tropical similar.

I like the below style, with no flamingos or pineapples . Colorful and leafy is good, preferably with leaves and flowers that are native to Tropical Queensland Australia.

Label 1. 1 kg rainforest Blend

This will be our standard table honey, I would like to have a vey striking colorful, cheerful design something like to the 2 examples above.

Must have Australian made logo on Side 2 , with words Australian Honey in it. See attached Australian made logo pick either portrait or landscape based on your design.

If you think the attached picture of the Pink Euodia is will help the labels appeal please feel free to use it.
Please See attached Document for content rainforest Honey Label 1 kg.

Barcode 0918273645501

Size of labels ae shown below. I would like 5mm radius on all corners. 15 mm allowance for curvature of bottle.
Side 1 Side 2 Side 3

65mm

Label 2. 1 kg Bloodwood and Scarlet Gum Blend

This will be another of our standard table honey, I would like to have a vey striking colorful, cheerful design something like to the 2 examples above.

Must have Australian made logo on Side 2 , with words Australian Honey in it. See attached Australian made logo pick either portrait or landscape based on your design

If you think the attached picture of the Scarlet Gum is will help the labels appeal please feel free to use it.

Please See attached Document for content Bloodwood and Scarlet Gum Blend Label 1 kg.
Barcode 0918273645518
Side 1 Side 2 Side 3

65mm

Label 3. 500 g rainforest Blend

Exactly the same as the 1 kg rainfest blend but the Net weight ill be changed to 500 grams.

If you think the attached picture of the Pink Euodia is ill help the labels appeal please feel free to use it.
Barcode 0918273645525
Side 1 Side 2 Side 3

65mm

Label 4. 500g Bloodwood and Scarlet Gum Blend

Exactly the same as the 1 kg “Bloodwood and Scarlet Gum Blend” but the Net weight ill be changed to 500 grams.

Barcode 0918273645532
Side 1 Side 2 Side 3

65mm

Label 5. 250g Manuka Honey Attached rough word document for layout and text

This will be our Sun Orchard Premium range of Honeys, A bonze, theme to denote the quality of honey. Printed on silver backed label paper, to give it a shiny appearance.

Main Points
• Bronze backing, see picture below for example from competitor.
• Silver backed labels paper.
• Must have the Australian made Logo on the Front of jar or side 2.
• Side 1 Australian map outline in the bronze backing color with a arrow to Cairns.
• Side 2 has logo “Sun Orchard” Name, Australian Manuka Honey, Leptospermum Polygalifolium Tropicum, Australian Made Logo (Australian Honey) see file “GrownProducedMade_PDF_P (1).pdf”, 250g, NPA+8, MGO 183
• Side 3 TEXT “Our Australian Manuka honey is sourced from pristine native leptospermum forests situated in tropical north Queensland.

Manuka honey gets it’s unique antibacterial properties from naturally occurring methylglyoxal (MGO). The higher the MGO rating the stronger antibacterial properties.”
• Side 4 Nutritional Information Table, Address, Barcode” 0918273645549”, Text “recycled container “with recycled logo

Barcode 0918273645549
First 3 side connected with 6 mm allowance for curvature of bottle, Side 4 separate. 5mm radius on all corners
Side 1 Side 2 Side 3 Side 4

50mm

Competitors labels for inspiration and example of Bronze Backing

*Business Card*
Sun Orchard “logo”

Medical Honey’s
Tropical Rainforest Honeys
Strong 5 Fames Nucleus Colonies all year round
Director Rupert Vasquez
Email: rvasquez.rv@examplemail.test
Mobile no. 0491 058 273
ABN 71596204318

Target Market(s)

Tourist visiting Cairns North Queensland Australia, both foreign mainly Chinese and tourist from Melbourne.

Contact Information for Business Card

Sun Orchard “logo”

Medical Honey’s
Tropical Rainforest Honey's
Director Rupert Vasquez
Mobile no. 0491 058 273
ABN 71596204318

Logo Text

Sun Orchard

Font styles to use
Script

Colors
00a990
f04a50
0255a3
9bcb3b
fbed22

Requirements
Must have
• Clean and Clear, must check all spelling, punctuation and Gram
Nice to have
• Lots of colour in labels but not too much content.
• O
• Manuka labels to be high end looking people are paying good money and should see it in the label.
• Other honey ranges can be colourful and playful. Topical relaxed, rainforest

```html
<!DOCTYPE html>
<html lang="en">
<head>
<meta charset="utf-8">
<title>Sun Orchard — Business Card</title>
<link href="https://fonts.googleapis.com/css2?family=Quicksand:wght@500;600&family=Dancing+Script:wght@600&display=swap" rel="stylesheet">
<style>
  :root {
    --page: #eef2ee;
    --card: #fbfcfb;
    --card-edge: #dfe5df;
    --leaf-green: #8cc63f;
    --sun-yellow: #f7c51e;
    --ink-grey: #5b5f5c;
  }
  * { margin: 0; padding: 0; box-sizing: border-box; }
  html, body {
    width: 1200px;
    height: 853px;
    overflow: hidden;
    background: var(--page);
    font-family: "Quicksand", sans-serif;
  }
  .canvas {
    position: relative;
    width: 1200px;
    height: 853px;
  }
  .card {
    position: absolute;
    width: 520px;
    height: 297px;
    background: var(--card);
    border: 1px solid var(--card-edge);
    box-shadow: 0 6px 14px rgba(60, 80, 60, 0.12);
    display: flex;
    flex-direction: column;
    align-items: center;
    justify-content: center;
  }
  .card--back { left: 70px; top: 80px; }
  .card--front { left: 380px; top: 470px; }

  .brand {
    display: flex;
    align-items: center;
    gap: 10px;
    color: var(--leaf-green);
    font-family: "Quicksand", sans-serif;
    font-weight: 600;
    white-space: nowrap;
  }
  .brand__dot {
    border-radius: 50%;
    background: var(--sun-yellow);
    flex: none;
  }
  .brand--small { font-size: 22px; margin-bottom: 14px; }
  .brand--small .brand__dot { width: 16px; height: 16px; }
  .brand--large { font-size: 48px; gap: 16px; }
  .brand--large .brand__dot { width: 34px; height: 34px; }
  .brand--standalone {
    position: absolute;
    left: 700px;
    top: 240px;
    font-size: 42px;
    gap: 14px;
  }
  .brand--standalone .brand__dot { width: 30px; height: 30px; }

  .services {
    list-style: none;
    text-align: center;
    color: var(--ink-grey);
    font-size: 12.5px;
    font-weight: 500;
    line-height: 1.35;
  }
  .person {
    margin: 12px 0 14px;
    color: var(--leaf-green);
    font-family: "Dancing Script", cursive;
    font-size: 28px;
    font-weight: 600;
  }
  .contact {
    color: var(--ink-grey);
    font-size: 12.5px;
    font-weight: 500;
  }
</style>
</head>
<body>
  <main class="canvas">
    <section class="card card--back" aria-label="Business card, back">
      <div class="brand brand--small">
        <span class="brand__dot"></span>
        <span class="brand__name">Sun Orchard</span>
      </div>
      <ul class="services">
        <li>Medical Honey's</li>
        <li>Tropical Rainforest Honeys</li>
        <li>Strong 5 Fames Nucleus Colonies to order</li>
      </ul>
      <p class="person">Rupert Vasquez / director</p>
      <p class="contact">rvasquez.rv@examplemail.test / 0491 058 273 / ABN 71596204318</p>
    </section>

    <div class="brand brand--standalone">
      <span class="brand__dot"></span>
      <span class="brand__name">Sun Orchard</span>
    </div>

    <section class="card card--front" aria-label="Business card, front">
      <div class="brand brand--large">
        <span class="brand__dot"></span>
        <span class="brand__name">Sun Orchard</span>
      </div>
    </section>
  </main>
</body>
</html>
```